Window company.

Hello,

We are a small family business located in Madrid, Spain that works nationwide to fix, change or mount the windows of your home / premises.

The group of possible clients to whom the flyer is focused ranges from 30 to 65 years, families in general who want comfort at home and extra savings every year in heating.

It must include not only graphics and a striking aesthetic in accordance with the concepts of wanting to reach / transmit the final product to the customer to sell the product.

Details to also include:

-Brief history of the company and its foundation in 2006. It will be subsequently translated into Spanish so put in words what you consider necessary so that the client stays with the concept that we are professionals.

--Specialized in exterior aluminum and PVC carpentry.

-We move to your home for a first visit and we provide the budget totally free without any commitment.

- Also payment facilities; up to 3 times, without interest.

-Contact details of the company. (WhatsApp, email, phone and location)
Open: Mon - Friday 11,00am - 9pm
Saturday: 12,00am - 7pm
Sunday: Closed

Also as a suggestion, to decide on your own, graphics of types of window openings, if you consider that anything that is striking for the client so it wonr be yet another advertising flyer.

We are open to all kinds of ideas, all of them involving marketing branding.

We are open to any type of idea and we want to stand out, the construction world is tough and we have an idea to grow, taking into account that it must not only be beautiful but commercial to attract potential customers with all kinds of purchasing power.

Thank you.

```html
<!DOCTYPE html>
<html lang="en">
<head>
<meta charset="utf-8">
<title>Ventalia Window Flyer</title>
<link rel="stylesheet" href="https://fonts.googleapis.com/css2?family=Open+Sans:wght@400;600;700&family=Roboto:wght@300;700;900&family=Poppins:wght@300;400&display=swap">
<style>
  :root {
    --page-bg: #cccccc;
    --paper: #ffffff;
    --brand-red: #d11f40;
    --silver-dark: #6d6d6d;
    --silver-light: #e4e4e4;
    --ink: #222222;
    --brand-grey: #b3ab9c;
    --footer-dark: #141416;
    --footer-mid: #2a2a2c;
  }
  * { margin: 0; padding: 0; box-sizing: border-box; }
  html, body { width: 1200px; height: 1200px; overflow: hidden; background: var(--page-bg); }
  .flyer {
    position: absolute; left: 250px; top: 104px;
    width: 700px; height: 990px;
    background: var(--paper); overflow: hidden;
    font-family: "Open Sans", sans-serif;
  }
  .flyer-shapes { position: absolute; inset: 0; }
  .brand {
    position: absolute; left: 50px; top: 42px;
    display: flex; align-items: center; gap: 12px;
  }
  .brand-mark { width: 18px; height: 18px; background: var(--brand-red); }
  .brand-name {
    font-family: "Roboto", sans-serif; font-weight: 700;
    font-size: 38px; letter-spacing: 1px; color: var(--brand-grey);
  }
  .quote-call {
    position: absolute; right: 38px; top: 24px; text-align: right;
    color: var(--brand-red); line-height: 26px;
  }
  .quote-call .label { font-size: 23px; font-weight: 400; }
  .quote-call .number { font-size: 23px; font-weight: 700; }
  .offer {
    position: absolute; left: 78px; top: 500px; width: 262px; color: #fff;
  }
  .offer-title {
    font-family: "Roboto", sans-serif; font-weight: 900;
    font-size: 22px; letter-spacing: -0.3px; line-height: 28px;
    padding-bottom: 7px; border-bottom: 1.5px solid #fff; width: 228px;
  }
  .offer-list { list-style: none; margin-top: 18px; }
  .offer-list li {
    position: relative; padding-left: 11px;
    font-size: 18.5px; font-weight: 600; line-height: 22.5px;
    margin-bottom: 23px;
  }
  .offer-list li::before {
    content: "·"; position: absolute; left: 0; top: -1px; font-size: 18px;
  }
  .why {
    position: absolute; left: 383px; top: 570px; width: 282px; color: var(--ink);
  }
  .why-title {
    display: flex; align-items: center; gap: 14px;
    font-family: "Roboto", sans-serif; font-size: 20px; font-weight: 300;
  }
  .why-title strong { font-weight: 700; }
  .why-title .rule { flex: 1; height: 2px; background: var(--ink); }
  .why-text {
    font-family: "Poppins", sans-serif; font-weight: 300;
    font-size: 13.3px; line-height: 16px; margin-top: 10px; letter-spacing: 0.3px;
  }
  .why-text + .why-text { margin-top: 16px; }
  .hours {
    display: grid; grid-template-columns: 50px auto; margin-top: 18px;
    font-size: 16.5px; font-weight: 700; line-height: 25px; color: var(--brand-red);
  }
  .hours .label { color: #000; font-weight: 600; grid-row: span 3; }
  .footer-address {
    position: absolute; left: 120px; top: 918px; width: 228px; text-align: center;
    font-family: "Poppins", sans-serif; font-size: 13.5px; line-height: 19px; color: #fff;
  }
  .footer-phone {
    position: absolute; left: 470px; top: 920px;
    font-family: "Roboto", sans-serif; font-weight: 700; font-size: 23px; color: #fff;
  }
</style>
</head>
<body>
<div class="flyer">
  <svg class="flyer-shapes" viewBox="0 0 700 990" width="700" height="990">
    <defs>
      <linearGradient id="silver" x1="0" x2="1" y1="0" y2="0">
        <stop offset="0" stop-color="var(--silver-dark)"/>
        <stop offset="0.45" stop-color="var(--silver-light)"/>
        <stop offset="1" stop-color="var(--silver-dark)"/>
      </linearGradient>
      <linearGradient id="interior" x1="0" x2="1" y1="0" y2="1">
        <stop offset="0" stop-color="#b9b6b1"/>
        <stop offset="0.4" stop-color="#d8d6d2"/>
        <stop offset="0.65" stop-color="#eef0f0"/>
        <stop offset="0.85" stop-color="#5b6577"/>
        <stop offset="1" stop-color="#a77a55"/>
      </linearGradient>
      <linearGradient id="footer" x1="0" x2="1">
        <stop offset="0" stop-color="var(--footer-mid)"/>
        <stop offset="1" stop-color="var(--footer-dark)"/>
      </linearGradient>
    </defs>

    <rect role="img" aria-label="Photo of a bright living and dining room with large white-framed windows, glass table and blue chairs" x="0" y="110" width="700" height="470" fill="url(#interior)"/>

    <!-- header waves -->
    <path d="M0,0 H700 V116 Q330,265 0,150 Z" fill="var(--brand-red)"/>
    <path d="M0,0 H700 V80 Q330,248 0,135 Z" fill="url(#silver)"/>
    <path d="M0,0 H700 V70 Q330,239 0,128 Z" fill="var(--paper)"/>

    <!-- lower left wedge -->
    <path d="M0,507 Q30,497 60,488 L60,540 Q25,550 0,560 Z" fill="var(--brand-red)"/>
    <path d="M0,559 Q25,548 60,534 L60,545 Q25,558 0,572 Z" fill="url(#silver)"/>
    <path d="M0,571 Q25,557 60,544 L60,877 L0,877 Z" fill="var(--paper)"/>

    <!-- lower right waves -->
    <path d="M346,478 Q520,488 700,536 V552 Q520,505 346,494 Z" fill="var(--brand-red)"/>
    <path d="M346,493 Q520,504 700,551 V566 Q520,511 346,500 Z" fill="url(#silver)"/>
    <path d="M346,499 Q520,510 700,565 V877 H346 Z" fill="var(--paper)"/>

    <!-- offer panel -->
    <path d="M51,473 H346 V877 H51 V495 L42,498 Z" fill="var(--brand-red)"/>

    <!-- footer -->
    <rect x="0" y="877" width="700" height="6" fill="var(--brand-red)"/>
    <rect x="0" y="883" width="700" height="107" fill="url(#footer)"/>

    <!-- pin icon -->
    <path d="M80,920 a13,13 0 0 1 13,13 c0,10 -13,25 -13,25 c0,0 -13,-15 -13,-25 a13,13 0 0 1 13,-13 Z" fill="var(--brand-red)"/>
    <circle cx="80" cy="932" r="5" fill="var(--footer-mid)"/>

    <!-- phone icon -->
    <path d="M432,921 l7,-3 l6,11 l-5,4 c2,6 7,11 13,14 l4,-5 l11,6 l-3,7 c-2,3 -7,4 -11,2 c-12,-6 -20,-15 -25,-26 c-1,-4 0,-8 3,-10 Z" fill="var(--brand-red)"/>
    <path d="M452,922 a10,10 0 0 1 10,10 M452,915 a17,17 0 0 1 17,17" stroke="var(--brand-red)" stroke-width="2.5" fill="none" stroke-linecap="round"/>
  </svg>

  <div class="brand">
    <span class="brand-name">VENTALIA</span>
    <span class="brand-mark"></span>
  </div>

  <div class="quote-call">
    <div class="label">Call us for free quote</div>
    <div class="number">+34 600 41 27 95</div>
  </div>

  <section class="offer">
    <h2 class="offer-title">WHAT WE OFFER?</h2>
    <ul class="offer-list">
      <li>Specialized in exterior aluminum and PVC carpentry.</li>
      <li>We move to your home for a first visit and we provide the budget totally free without any commitment.</li>
      <li>Also payment facilities; up to 3 times, without interest.</li>
    </ul>
  </section>

  <section class="why">
    <h2 class="why-title"><span>WHY <strong>US?</strong></span><span class="rule"></span></h2>
    <p class="why-text">We are a small family business located in Madrid, Spain that works nationwide to fix, change or mount the windows of your home / premises. We are founded in 2006.</p>
    <p class="why-text">We offer full service from initial contact to final fitting, making sure all projects are finished to the highest standard.</p>
    <div class="hours">
      <span class="label">Open:</span>
      <span>Mon - Friday 11,00am - 9pm</span>
      <span>Saturday: 12,00am - 7pm</span>
      <span>Sunday: Closed</span>
    </div>
  </section>

  <address class="footer-address" style="font-style:normal">
    Pol. Ind. Valdelobos III (4,182.60 mi)<br>Valdelobos, Spain 28340
  </address>
  <div class="footer-phone">+34 600 41 27 95</div>
</div>
</body>
</html>
```